Gestaltung Flyer & Infokärtchen für Tellerbund
Zielgruppe
Hungrige Personen im Geschäft/Firma (keine Privatpersonen zu Hause), welche Menüs bestellen wollen. Die Menüs dürfen nicht zuviel kosten, aber der Flyer darf deshalb auch nicht "billig" daher kommen. Im Gegenteil.
Aufgabenstellung
Tellerbund - Deine Food Community ist eine seite, die virtuelle Bestellgemeinschaften schafft und damit Lieferpauschalen und Mindestbestellmengen für den Einzelbesteller umgeht. Der Einzelbesteller kennt also seine "Mitbesteller" nicht. Zudem wird das Menü günstiger, je mehr Leute in seiner Community bestellen. Diese Mitbesteller sind andere Personen in der gleichen Firma oder direkte Nachbarfirmen. In jedem Fall geht es um Bestellung von warmen Menüs.
Enorm wichtig und absolut zentral bei dem Infoflyer A4 UND dem kleinen Infokärtchen (A6 gefaltet mit aussen hinten weiss, aussen vorne Hauptmessage mit Logo (seperater Wettbewerb) und Innen zentrale Messages mit Internetseite www.TBM.ch) ist:
1. Der zentrale Unterschied zu anderen Bestellsystemen. warum der Kunde bei uns bestellen soll. Aus 2 Gründen!
1. "Keine Lieferpauschale", "Keine Mindestbestellmenge", "Punkte sammeln". Keine Lieferpauschale und keine Mindestbestellmenge - auch wenn nur 1 Menü bestellt wird. Bei Jedem Kauf kann der Besteller Punkte sammeln und diese dann in gratis Menü umwandeln. Zudem sammelt auch die virtuelle Bestellgemeinschaft punkte. Bei Erreichen von xy Punkten wird in der Community Preise verlost.
2. Community Gedanke: Je mehr bestellt wird, desto günstiger wird der Preis - bis zu einem bestimmten Minimum. Bei ersten Besteller kostet also bspw. das Menü warm geliefert all inkl. 15 Euro; bis minimum 9 Euro. Es muss aber voraus bezahlt werden (diese info muss aber ncht unbedingt auch drauf).
Beispiele für den Community Gedanken wären:
- "Tellerbund - Deine Food Community - Je mehr bestellen, desto günstiger wird’s"
- "Tellerbund - Deine Food Community - Andere bestellen - Du profitierst"
- "Tellerbund - Deine Food Community - Du bist teil der Community - mehr Besteller - günstiger Preis" etc.
- oder man stellt dies bildlich dar zusammen bspw. mit text 1 (ich stelle mir bspw. vor, 1 männchen hoher Preis ($ oben auf berg) und..

```html
<!DOCTYPE html>
<html lang="de">
<head>
<meta charset="utf-8">
<title>Tellerbund – Infokärtchen Titel und Rückseite</title>
<link rel="stylesheet" href="https://fonts.googleapis.com/css2?family=Nunito:wght@400;700;800;900&family=Caveat:wght@500;600&display=swap">
<style>
  :root {
    --page: #ffffff;
    --sky-top: #c9dcea;
    --sky-bottom: #eef4f9;
    --swirl: rgba(255,255,255,0.55);
    --headline-blue: #3b82c4;
    --ink-red: #c8281f;
    --ink-blue: #3d6fb8;
    --note-green: #e3f0c8;
    --note-edge: #c9dfa0;
    --napkin: #f4f4f2;
    --band-green: #9cc35a;
    --band-green-light: #c5dd94;
    --button-green: #8fbc45;
    --button-green-dark: #6f9a2c;
    --food-warm: #e9c25a;
    --food-green: #6f9b3a;
    --cursor-stroke: #333333;
    --caption: #222222;
  }
  * { box-sizing: border-box; margin: 0; padding: 0; }
  html, body { width: 1200px; height: 1200px; overflow: hidden; background: var(--page); }
  .sheet { position: relative; width: 1200px; height: 1200px; }

  .card {
    position: absolute; top: 180px; width: 551px; height: 788px; overflow: hidden;
    background: linear-gradient(170deg, var(--sky-top) 0%, var(--sky-bottom) 70%, #f7fafc 100%);
    box-shadow: 0 2px 6px rgba(0,0,0,0.18);
  }
  .card--front { left: 37px; }
  .card--back { left: 612px; }
  .scene { position: absolute; left: 0; top: 0; }

  .caption {
    position: absolute; top: 1058px; width: 551px; text-align: center;
    font: 400 34px/1 "Nunito", Arial, sans-serif; color: var(--caption);
  }
  .caption--front { left: 37px; }
  .caption--back { left: 612px; }

  .note {
    position: absolute; left: 52px; top: 24px; width: 234px; height: 196px;
    background: var(--note-green); border: 1px solid var(--note-edge);
    box-shadow: 2px 3px 6px rgba(0,0,0,0.15); transform: rotate(-3deg);
    padding: 34px 10px 0 20px;
  }
  .note__list { list-style: none; font: 600 22px/1.05 "Caveat", cursive; color: var(--ink-red); }
  .note__list li { margin-bottom: 8px; white-space: nowrap; }
  .note__list li.wrap { white-space: normal; }

  .napkin {
    position: absolute; background: var(--napkin);
    box-shadow: -3px 4px 8px rgba(0,0,0,0.15);
  }
  .napkin--front { left: 300px; top: -20px; width: 270px; height: 255px; transform: rotate(-6deg); }
  .napkin--back { left: -20px; top: 490px; width: 380px; height: 212px; transform: rotate(-4deg); }

  .brand {
    position: absolute; font: 900 26px/1 "Nunito", Arial, sans-serif; color: var(--ink-blue);
    display: flex; align-items: center; gap: 8px;
  }
  .brand__dot { width: 18px; height: 18px; border-radius: 50%; background: var(--band-green); }
  .brand--front { left: 360px; top: 92px; transform: rotate(-6deg); }
  .brand--back { left: 235px; top: 530px; font-size: 17px; transform: rotate(-4deg); }
  .brand--back .brand__dot { width: 12px; height: 12px; }

  .headline {
    position: absolute; font-family: "Nunito", Arial, sans-serif; font-weight: 900;
    color: var(--headline-blue); white-space: nowrap;
    text-shadow: 0 0 3px #fff, 0 0 3px #fff, 0 0 6px #fff, 0 0 8px #fff;
  }
  .headline span { display: block; }
  .headline--front { left: 45px; top: 290px; font-size: 68px; line-height: 66px; }
  .headline--front .line-2 { padding-left: 60px; }
  .headline--back { left: 73px; top: 258px; font-size: 46px; line-height: 48px; }
  .headline--back .line-2 { padding-left: 27px; }

  .cta {
    position: absolute; left: 190px; top: 460px; width: 178px; height: 48px; border-radius: 12px;
    background: linear-gradient(var(--band-green-light), var(--button-green));
    border: 2px solid var(--button-green-dark);
    font: 800 21px/44px "Nunito", Arial, sans-serif; color: #fff; text-align: center;
  }
  .cta-pointer { position: absolute; left: 320px; top: 498px; }

  .photo {
    position: absolute; left: 0; top: 562px; width: 315px; height: 180px;
    border-radius: 0 60% 40% 0 / 0 50% 50% 0;
    background: radial-gradient(ellipse at 45% 50%, var(--food-warm) 0%, #d9a93f 40%, var(--food-green) 75%, #f3eee0 100%);
  }

  .imprint {
    position: absolute; left: 28px; top: 585px; transform: rotate(-6deg); transform-origin: left top;
    font: 500 19px/1.15 "Caveat", cursive; color: var(--ink-blue);
  }

  .url {
    position: absolute; left: 37px; top: 744px;
    font: 800 21px/1 "Nunito", Arial, sans-serif; color: #fff;
  }
</style>
</head>
<body>
<div class="sheet">

  <section class="card card--front">
    <svg class="scene" width="551" height="788" viewBox="0 0 551 788" aria-hidden="true">
      <defs>
        <path id="cursor" d="M0 0 L0 24 L6 18 L10.5 28 L15 26 L10.5 16 L18 16 Z"
              fill="#fff" stroke="var(--cursor-stroke)" stroke-width="1.4" stroke-linejoin="round"/>
      </defs>
      <circle cx="520" cy="360" r="420" fill="none" stroke="var(--swirl)" stroke-width="70"/>
      <path d="M0 690 C170 660 360 690 551 620 L551 788 L0 788 Z" fill="var(--band-green-light)"/>
      <path d="M0 742 C200 730 380 740 551 700 L551 788 L0 788 Z" fill="var(--band-green)"/>
      <g class="cursors">
        <use href="#cursor" x="345" y="580"/><use href="#cursor" x="380" y="565"/>
        <use href="#cursor" x="420" y="590"/><use href="#cursor" x="460" y="570"/>
        <use href="#cursor" x="500" y="590"/><use href="#cursor" x="530" y="560"/>
        <use href="#cursor" x="360" y="620"/><use href="#cursor" x="400" y="630"/>
        <use href="#cursor" x="440" y="620"/><use href="#cursor" x="480" y="635"/>
        <use href="#cursor" x="520" y="615"/><use href="#cursor" x="330" y="660"/>
        <use href="#cursor" x="370" y="670"/><use href="#cursor" x="410" y="665"/>
        <use href="#cursor" x="450" y="675"/><use href="#cursor" x="490" y="665"/>
        <use href="#cursor" x="530" y="670"/><use href="#cursor" x="300" y="700"/>
        <use href="#cursor" x="345" y="710"/><use href="#cursor" x="390" y="715"/>
        <use href="#cursor" x="430" y="710"/><use href="#cursor" x="470" y="720"/>
        <use href="#cursor" x="510" y="710"/><use href="#cursor" x="280" y="745"/>
        <use href="#cursor" x="325" y="755"/><use href="#cursor" x="370" y="750"/>
        <use href="#cursor" x="410" y="755"/><use href="#cursor" x="455" y="750"/>
        <use href="#cursor" x="500" y="755"/><use href="#cursor" x="535" y="740"/>
      </g>
    </svg>

    <div class="note">
      <ul class="note__list">
        <li>– Keine Mindestbestellung</li>
        <li>– Keine Lieferpauschal</li>
        <li class="wrap">–Essen und Punkte sammeln</li>
      </ul>
    </div>

    <div class="napkin napkin--front" role="img" aria-label="Papierserviette"></div>
    <div class="brand brand--front"><span class="brand__dot"></span>Tellerbund</div>

    <h1 class="headline headline--front"><span>Schlemmen</span><span class="line-2">und Punkten</span></h1>
    <div class="cta">jetzt sparen</div>
    <svg class="cta-pointer" width="22" height="32" viewBox="-2 -2 22 32" aria-hidden="true">
      <path d="M0 0 L0 24 L6 18 L10.5 28 L15 26 L10.5 16 L18 16 Z"
            fill="#fff" stroke="var(--cursor-stroke)" stroke-width="1.4" stroke-linejoin="round"/>
    </svg>
    <div class="photo" role="img" aria-label="Foto eines Tellers Pasta mit Tomaten, Bohnen und Käse"></div>

    <div class="url">www.TBM.ch</div>
  </section>

  <section class="card card--back">
    <svg class="scene" width="551" height="788" viewBox="0 0 551 788" aria-hidden="true">
      <defs>
        <path id="cursor-b" d="M0 0 L0 24 L6 18 L10.5 28 L15 26 L10.5 16 L18 16 Z"
              fill="#fff" stroke="var(--cursor-stroke)" stroke-width="1.4" stroke-linejoin="round"/>
      </defs>
      <circle cx="520" cy="360" r="420" fill="none" stroke="var(--swirl)" stroke-width="70"/>
      <path d="M0 690 C170 660 360 690 551 620 L551 788 L0 788 Z" fill="var(--band-green-light)"/>
      <path d="M0 742 C200 730 380 740 551 700 L551 788 L0 788 Z" fill="var(--band-green)"/>
      <g class="cursors">
        <use href="#cursor-b" x="375" y="367"/><use href="#cursor-b" x="471" y="472"/>
        <use href="#cursor-b" x="410" y="565"/><use href="#cursor-b" x="450" y="545"/>
        <use href="#cursor-b" x="495" y="560"/><use href="#cursor-b" x="530" y="530"/>
        <use href="#cursor-b" x="380" y="610"/><use href="#cursor-b" x="425" y="615"/>
        <use href="#cursor-b" x="465" y="600"/><use href="#cursor-b" x="505" y="610"/>
        <use href="#cursor-b" x="535" y="590"/><use href="#cursor-b" x="385" y="660"/>
        <use href="#cursor-b" x="430" y="655"/><use href="#cursor-b" x="470" y="665"/>
        <use href="#cursor-b" x="510" y="655"/><use href="#cursor-b" x="395" y="705"/>
        <use href="#cursor-b" x="440" y="710"/><use href="#cursor-b" x="485" y="705"/>
        <use href="#cursor-b" x="525" y="700"/><use href="#cursor-b" x="290" y="748"/>
        <use href="#cursor-b" x="335" y="752"/><use href="#cursor-b" x="380" y="748"/>
        <use href="#cursor-b" x="425" y="755"/><use href="#cursor-b" x="470" y="748"/>
        <use href="#cursor-b" x="515" y="752"/>
      </g>
    </svg>

    <h2 class="headline headline--back"><span>hmm... morgen</span><span class="line-2">gleich nochmal!</span></h2>

    <div class="napkin napkin--back" role="img" aria-label="Papierserviette mit handgeschriebenem Impressum"></div>
    <div class="brand brand--back"><span class="brand__dot"></span>Tellerbund</div>
    <p class="imprint">
      Impressum:<br>
      „Tellerbund – powered by Valmora S.A.,<br>
      Lindenweg 14, 8045 Zürich,<br>
      info@tellerbund.ch
    </p>

    <div class="url">www.TBM.ch</div>
  </section>

  <p class="caption caption--front">Titel</p>
  <p class="caption caption--back">Rückseite</p>
</div>
</body>
</html>
```